Business card and stationary package

Travel management company looking for designs for single sided business cards, letterhead and envelope. Looking for contemporary designs using our existing logo. Design should clean, not trendy, no gradation of colors and no graphic other than the icon from the logo. Nothing complicated or difficult to read. Should be a crisp design using blue, gray and black colors only.
Letterhead should include a Word template and PDF template.
Business cards are one sided as the reverse will be dynamic images in our company portfolio of images.
We will use the same designer periodically for design projects using the same style guide for upcoming projects as well. Prefer working with designer that will assist with website, brochures and other marketing materials.

Logo Colors and Font:
Blue: 2189c6 Color Hex
Gray: 666666 Color Hex 60% Black
Black: 100% Black
Font: Century Gothic

Target Market(s)

business-to-business

Industry/Entity Type

Travel Industry

Contact Information for Business Card

Sample information for business cards will be:

Daniel Fenwick
Managing Partner

Harborline Journey Services, Inc.
274 Alder Lane, Suite 3621
Alder Cove, ME 04187

207-555-0148 Direct Dial
207-555-0193 Fax

daniel@harborlinejourney.net
www.harborlinejourney.net

Font styles to use
Sans Serif

Requirements
Must have
• Clean, crisp design, easy to ready, memorable.
Nice to have
• We tend to like dynamic designs that are simple, not trendy, contemporary and easy to read.
Should not have
• no gradation of colors and no graphic other than the icon from the logo, no background images
• **Note that the background should only be white. No black/gary backgrounds or graded colors**

```html
<!DOCTYPE html>
<html lang="en">
<head>
<meta charset="utf-8">
<title>Harborline Journey Services – Stationery</title>
<link href="https://fonts.googleapis.com/css2?family=Questrial&display=swap" rel="stylesheet">
<style>
  :root {
    --backdrop: #676767;
    --paper: #ffffff;
    --blue: #2189c6;
    --gray: #666666;
    --mark-faint: #ebebeb;
    --edge: rgba(150, 165, 165, 0.22);
  }
  * { box-sizing: border-box; margin: 0; padding: 0; }
  html, body { width: 1200px; height: 844px; overflow: hidden; }
  body {
    position: relative;
    background: var(--backdrop);
    font-family: "Questrial", "Century Gothic", sans-serif;
    color: var(--gray);
  }
  .sheet {
    position: absolute;
    background: var(--paper);
    overflow: hidden;
    box-shadow: inset 0 0 60px var(--edge);
  }
  .letterhead { left: 42px; top: 72px; width: 496px; height: 700px; }
  .envelope   { left: 557px; top: 72px; width: 602px; height: 356px; }
  .card       { left: 557px; top: 445px; width: 213px; height: 118px; box-shadow: inset 0 0 20px var(--edge); }

  .backdrop-disc {
    position: absolute;
    border-radius: 50%;
    background: var(--mark-faint);
  }
  .letterhead .backdrop-disc { left: 4px; top: -66px; width: 276px; height: 276px; }
  .envelope .backdrop-disc   { left: -10px; top: -60px; width: 248px; height: 248px; }
  .card .backdrop-disc       { left: 123px; top: -13px; width: 80px; height: 80px; }

  .brand {
    position: absolute;
    display: flex;
    align-items: center;
    white-space: nowrap;
  }
  .brand-dot {
    border-radius: 50%;
    background: var(--blue);
    flex: none;
  }
  .brand-name { color: var(--gray); letter-spacing: 0.03em; line-height: 1; }

  .letterhead .brand { left: 26px; top: 36px; gap: 8px; }
  .letterhead .brand-dot { width: 30px; height: 30px; }
  .letterhead .brand-name { font-size: 24px; }

  .envelope .brand { left: 22px; top: 44px; gap: 7px; }
  .envelope .brand-dot { width: 27px; height: 27px; }
  .envelope .brand-name { font-size: 20px; }

  .card .brand { left: 6px; top: 76px; gap: 5px; }
  .card .brand-dot { width: 20px; height: 20px; }
  .card .brand-name { font-size: 10px; }

  .contact-block {
    position: absolute;
    left: 307px; top: 24px;
    padding: 3px 0 3px 7px;
    border-left: 1px solid var(--blue);
    font-size: 9.4px;
    line-height: 11.1px;
    list-style: none;
  }

  .card-details {
    position: absolute;
    right: 112px; top: 10px;
    text-align: right;
    font-size: 5.4px;
    line-height: 7px;
  }
  .card-details p + p { margin-top: 4px; }
  .card-rule {
    position: absolute;
    left: 106px; top: 7px;
    width: 1px; height: 66px;
    background: var(--blue);
  }
  .card-person { position: absolute; left: 114px; top: 9px; }
  .card-name { color: var(--blue); font-size: 10.4px; line-height: 12px; }
  .card-title { font-size: 7px; line-height: 8px; padding-left: 3px; }
</style>
</head>
<body>

  <section class="sheet letterhead" aria-label="Letterhead">
    <div class="backdrop-disc" aria-hidden="true"></div>
    <div class="brand">
      <span class="brand-dot"></span>
      <span class="brand-name">HARBORLINE</span>
    </div>
    <ul class="contact-block">
      <li>Harborline Journey Services, Inc.</li>
      <li>274 Alder Lane, Suite 3621</li>
      <li>Alder Cove, ME 04187</li>
      <li>207-555-0148 Direct Dial</li>
      <li>207-555-0193 Fax</li>
      <li>daniel@harborlinejourney.net</li>
      <li>www.harborlinejourney.net</li>
    </ul>
  </section>

  <section class="sheet envelope" aria-label="Envelope">
    <div class="backdrop-disc" aria-hidden="true"></div>
    <div class="brand">
      <span class="brand-dot"></span>
      <span class="brand-name">HARBORLINE</span>
    </div>
  </section>

  <section class="sheet card" aria-label="Business card">
    <div class="backdrop-disc" aria-hidden="true"></div>
    <div class="card-details">
      <p>Harborline Journey Services, Inc.<br>274 Alder Lane, Suite 3621<br>Alder Cove, ME 04187</p>
      <p>207-555-0148 Direct Dial<br>207-555-0193 Fax</p>
      <p>daniel@harborlinejourney.net<br>www.harborlinejourney.net</p>
    </div>
    <div class="card-rule"></div>
    <div class="card-person">
      <p class="card-name">Daniel Fenwick</p>
      <p class="card-title">Managing Partner</p>
    </div>
    <div class="brand">
      <span class="brand-dot"></span>
      <span class="brand-name">HARBORLINE</span>
    </div>
  </section>

</body>
</html>
```